Website Creation for Auto Repair Marketing Company - Brightpath Outreach Co

This will be a website and logo for a digital marketing agency servicing the auto repair industry.

Focus on modern, efficient, and easy to understand navigation and flow. We want users to easily sign up for our Review Software and a Visibility Audit on the site. Most of the people on this site will be male and between 30-50 years old.

Industry/Entity Type

Auto Repair

Number of Pages Required

1 page

Colors

Designer to choose colors to be used in the design.

```html
<!DOCTYPE html>
<html lang="en">
<head>
<meta charset="utf-8">
<title>Brightpath Outreach Co – Auto Repair Marketing</title>
<link href="https://fonts.googleapis.com/css2?family=Nunito+Sans:wght@300;400;600;700;800;900&display=swap" rel="stylesheet">
<style>
:root{
  --navy:#0b0b7c;
  --navy-deep:#08086a;
  --royal:#2c4fa3;
  --royal-dark:#233f8c;
  --text:#222;
  --muted:#555;
  --light:#f3f3f3;
  --star:#f06a1b;
  --white:#fff;
}
*{margin:0;padding:0;box-sizing:border-box}
html,body{width:1200px;height:5017px;overflow:hidden}
body{font-family:"Nunito Sans",Arial,sans-serif;color:var(--text);background:var(--white);position:relative}
.abs{position:absolute}
.btn{position:absolute;display:flex;align-items:center;justify-content:center;background:var(--royal);color:var(--white);font-weight:800;font-size:13px;border-radius:24px;letter-spacing:.3px}

/* header */
.site-header{top:0;left:0;width:1200px;height:101px}
.brand{left:76px;top:32px;font-size:33px;font-weight:600;color:#1a1a1a}
.header-tools{right:76px;top:44px;display:flex;align-items:center;gap:20px;font-size:13px;color:#222}
.dot-icon{width:12px;height:12px;border-radius:50%;background:#222}
.mail{display:flex;align-items:center;gap:6px}
.flags{display:flex;gap:4px}
.flags span{width:14px;height:9px;display:block}
.main-nav{top:101px;left:0;width:1200px;height:59px;background:var(--navy);display:flex;align-items:center;padding-left:76px;gap:31px}
.main-nav a{color:var(--white);font-size:13px;text-decoration:none;font-weight:600}

/* hero */
.hero{top:160px;left:0;width:1200px;height:574px;background:linear-gradient(120deg,#c8704b 0%,#5a5f80 30%,#3d4a68 60%,#2c3b52 100%)}
.hero-shade{inset:0;background:linear-gradient(180deg,rgba(0,0,30,.15),rgba(10,40,60,.35))}
.hero-title{top:180px;left:0;width:1200px;text-align:center;font-size:37px;font-weight:800;color:var(--white)}
.hero .btn{top:252px;height:54px;font-size:18px;font-weight:600;border-radius:28px}
.btn-signup{left:384px;width:210px;background:var(--navy)}
.btn-contact{left:604px;width:212px;background:var(--royal)}
.hero-arrow{top:205px}

/* sections */
.section-title{left:0;width:1200px;text-align:center;font-size:37px;font-weight:900;color:var(--navy)}
.welcome-text{top:864px;left:110px;width:980px;text-align:center;font-size:13.5px;line-height:22px;color:#333}
.video{top:1110px;left:130px;width:940px;height:511px;background:linear-gradient(135deg,#1c1c1c,#4a4038 45%,#8b7a66 70%,#2c2a28)}
.play{left:565px;top:1330px;width:70px;height:70px;border-radius:50%;background:var(--royal);display:flex;align-items:center;justify-content:center}

.services{top:1671px;left:0;width:1200px;height:665px;background:linear-gradient(135deg,#2a2f8e,#2b2e95 50%,#3a3fa2)}
.services .section-title{color:var(--white);top:98px}
.service-card{top:254px;width:347px;height:247px;background:var(--light)}
.service-card p{position:absolute;top:120px;left:30px;right:30px;text-align:center;font-size:14px;line-height:19px;color:#333}
.service-icon{top:200px;width:156px;height:156px;border-radius:50%;background:var(--royal);display:flex;align-items:center;justify-content:center}
.carousel-dots{top:582px;left:0;width:1200px;display:flex;justify-content:center;gap:17px}
.carousel-dots span{width:11px;height:11px;border-radius:50%;background:#3f45a8}
.carousel-dots span.on{background:#8a8fcf}

.reviews-sub{top:2448px;left:0;width:1200px;text-align:center;font-size:14px;color:#555}
.review-card{top:2503px;width:248px;height:345px;background:var(--light)}
.review-photo{top:0;left:0;width:248px;height:175px;background:linear-gradient(135deg,#2c3445,#6b7384 60%,#9aa2ae)}
.avatar{right:16px;top:95px;width:60px;height:60px;border-radius:50%;background:#c9b8a5;border:3px solid #fff}
.review-card h4{position:absolute;top:190px;left:18px;right:18px;font-size:11.5px;font-weight:800;color:#333;line-height:18px}
.review-card p{position:absolute;top:243px;left:18px;right:18px;font-size:11.5px;line-height:19px;color:#666}
.read-more{position:absolute;top:318px;left:18px;font-size:10px;font-weight:900;color:var(--royal)}
.stars{position:absolute;top:314px;right:20px;display:flex;gap:4px}
.round-arrow{top:2887px;width:28px;height:28px;border-radius:50%;display:flex;align-items:center;justify-content:center}
.view-all{top:2887px;left:1034px;width:105px;height:29px;background:var(--navy);color:#fff;font-size:10px;font-weight:900;display:flex;align-items:center;justify-content:center}

.software{top:3008px;left:0;width:1200px;height:758px;background:var(--navy)}
.software-photo{top:0;left:0;width:549px;height:758px;background:linear-gradient(150deg,#b01818 0%,#3a0e14 22%,#121a30 50%,#2d5aa8 75%,#d8cfc4 100%)}
.software h2{position:absolute;top:152px;left:660px;font-size:45px;line-height:55px;font-weight:800;color:#fff}
.software .lead{position:absolute;top:278px;left:660px;width:460px;font-size:16px;line-height:27px;color:#fff;font-weight:600}
.software .body{position:absolute;top:364px;left:660px;width:470px;font-size:15px;line-height:28px;color:#c7c9ee;font-weight:300}
.software .read{position:absolute;top:552px;left:660px;width:198px;height:60px;background:var(--royal);color:#fff;display:flex;align-items:center;justify-content:center;font-size:17px;letter-spacing:1px}

.map{top:3766px;left:0;width:1200px;height:448px;background:linear-gradient(135deg,#e6e6e6,#f2f2f2 50%,#e3e3e3)}
.map-card{top:227px;left:428px;width:188px;height:90px;background:#fff;box-shadow:0 2px 8px rgba(0,0,0,.15);padding:20px 34px;font-size:14px;line-height:25px;color:#444}
.map-btn{top:340px;width:56px;height:56px;background:#fff;border-radius:4px;display:flex;align-items:center;justify-content:center;box-shadow:0 2px 6px rgba(0,0,0,.15)}

.stat{top:4370px;width:260px;text-align:center}
.stat .num{font-size:72px;font-weight:300;color:#333;line-height:80px}
.stat .label{font-size:21px;font-weight:700;color:var(--royal);margin-top:10px}
.stat .btn{position:relative;margin:26px auto 0;width:142px;height:42px}

.site-footer{top:4638px;left:0;width:1200px;height:379px;background:var(--navy)}
.footer-nav{top:97px;left:0;width:1200px;display:flex;justify-content:center;gap:30px}
.footer-nav a{color:#fff;font-size:13px;text-decoration:none}
.socials{top:142px;left:0;width:1200px;display:flex;justify-content:center;gap:28px}
.socials span{width:18px;height:18px;border-radius:50%;background:#fff;display:block}
.newsletter{top:199px;left:325px;width:548px;height:58px;background:#fff;border-radius:4px}
.newsletter .field{position:absolute;left:75px;top:20px;font-size:12px;color:#555}
.newsletter .join{position:absolute;right:10px;top:11px;width:72px;height:37px;background:var(--royal);border-radius:4px;color:#fff;font-size:12px;font-weight:800;display:flex;align-items:center;justify-content:center}
.copyright{top:304px;left:0;width:1200px;text-align:center;color:#fff;font-size:11px}
</style>
</head>
<body>

<header class="site-header abs">
  <div class="brand abs">Brightpath Outreach Co</div>
  <div class="header-tools abs">
    <span class="dot-icon"></span>
    <span class="dot-icon"></span>
    <span class="mail">
      <svg width="14" height="10" viewBox="0 0 14 10"><rect x=".5" y=".5" width="13" height="9" fill="none" stroke="#222"/><path d="M.5 .5 7 6 13.5 .5" fill="none" stroke="#222"/></svg>
      hello@brightpathoutreach.com
    </span>
    <span class="flags"><span style="background:linear-gradient(#111 33%,#d00 33% 66%,#fc0 66%)"></span><span style="background:#203a8a"></span><span style="background:linear-gradient(#fff 50%,#d7141a 50%)"></span></span>
  </div>
</header>
<nav class="main-nav abs">
  <a href="#">HOME</a><a href="#">ABOUT US</a><a href="#">SERVICES</a><a href="#">REVIEWS</a><a href="#">CONTACT US</a>
</nav>

<section class="hero abs" role="img" aria-label="Mechanic fitting a car wheel with a glowing network graphic overlay">
  <div class="hero-shade abs"></div>
  <svg class="hero-arrow abs" style="left:72px" width="22" height="32" viewBox="0 0 22 32"><path d="M18 3 5 16l13 13" fill="none" stroke="#fff" stroke-width="5"/></svg>
  <svg class="hero-arrow abs" style="right:72px" width="22" height="32" viewBox="0 0 22 32"><path d="M4 3l13 13L4 29" fill="none" stroke="#fff" stroke-width="5"/></svg>
  <h1 class="hero-title abs">We are a Auto Repair Marketing</h1>
  <div class="btn btn-signup">SIGN UP</div>
  <div class="btn btn-contact">CONTACT US</div>
</section>

<h2 class="section-title abs" style="top:792px">WELCOME TO OUR WEBSITE</h2>
<p class="welcome-text abs">Et harum quidem rerum facilis est et expedita distinctio. Nam libero tempore, cum soluta nobis est eligendi optio cumque nihil impedit quo minus id quod maxime placeat facere possimus, omnis voluptas assumenda est, omnis dolor repellendus. Temporibus autem quibusdam et aut officiis debitis aut rerum necessitatibus saepe eveniet ut et voluptates repudiandae sint et molestiae non recusandae. Itaque earum rerum</p>
<div class="btn" style="top:948px;left:530px;width:140px;height:42px">LEARN MORE</div>

<h2 class="section-title abs" style="top:1038px">HOW IT WORKS</h2>
<div class="video abs" role="img" aria-label="Video still: smiling couple looking at a tablet inside a car"></div>
<div class="play abs"><svg width="22" height="26" viewBox="0 0 22 26"><path d="M3 2l17 11L3 24z" fill="#fff"/></svg></div>

<section class="services abs" role="img" aria-label="Services section over a blue-tinted photo of a car interior">
  <h2 class="section-title abs">SERVICES</h2>
  <div class="service-card abs" style="left:60px"><p>At vero eos et accusamus et iusto odio dignissimos ducimus qui blanditiis praesentium voluptatum.</p></div>
  <div class="service-card abs" style="left:427px"><p>At vero eos et accusamus et iusto odio dignissimos ducimus qui blanditiis praesentium voluptatum.</p></div>
  <div class="service-card abs" style="left:792px"><p>At vero eos et accusamus et iusto odio dignissimos ducimus qui blanditiis praesentium voluptatum.</p></div>
  <div class="service-icon abs" style="left:156px">
    <svg width="100" height="90" viewBox="0 0 100 90" fill="none" stroke="#fff" stroke-width="3"><circle cx="38" cy="30" r="18"/><circle cx="38" cy="30" r="7"/><path d="M14 70l8-14h50l8 14v10H14z"/><circle cx="28" cy="80" r="5"/><circle cx="66" cy="80" r="5"/><path d="M66 28h22M70 36h16"/></svg>
  </div>
  <div class="service-icon abs" style="left:522px">
    <svg width="90" height="90" viewBox="0 0 90 90" fill="none" stroke="#fff" stroke-width="3"><circle cx="45" cy="45" r="36"/><path d="M28 62l34-34M62 28l6-6M30 28l32 32M26 24l6 6"/></svg>
  </div>
  <div class="service-icon abs" style="left:888px">
    <svg width="96" height="90" viewBox="0 0 96 90" fill="none" stroke="#fff" stroke-width="3"><path d="M8 32 48 8l40 24v50H8z"/><path d="M20 38h56v44H20z"/><path d="M30 66l6-10h24l6 10v10H30z"/><path d="M20 46h56"/></svg>
  </div>
  <div class="carousel-dots abs"><span></span><span class="on"></span><span></span><span></span></div>
</section>

<h2 class="section-title abs" style="top:2386px">REVIEWS</h2>
<p class="reviews-sub abs">Lorem ipsum dolor sit amet, in error abhorreant</p>

<article class="review-card abs" style="left:60px">
  <div class="review-photo abs" role="img" aria-label="Mechanic working on an engine"><div class="avatar abs" role="img" aria-label="Reviewer portrait"></div></div>
  <h4>SED UT PERSPICIATIS UNDE OMNIS ISTE NATUS.</h4>
  <p>Lorem ipsum dolor sit amet, consectetur adipisicing elit, sed do eiusmod tempor incidid.</p>
  <span class="read-more">READ MORE »</span>
  <div class="stars"><svg width="72" height="14" viewBox="0 0 72 14"><g fill="#f06a1b"><path id="s" d="M7 0l2 5h5l-4 3 1.5 5L7 10l-4.5 3L4 8 0 5h5z"/><use href="#s" x="19"/><use href="#s" x="38"/><use href="#s" x="57"/></g></svg></div>
</article>
<article class="review-card abs" style="left:337px">
  <div class="review-photo abs" role="img" aria-label="Mechanic's hands with tools"><div class="avatar abs" role="img" aria-label="Reviewer portrait"></div></div>
  <h4>SED UT PERSPICIATIS UNDE OMNIS ISTE NATUS.</h4>
  <p>Lorem ipsum dolor sit amet, consectetur adipisicing elit, sed do eiusmod tempor incidid.</p>
  <span class="read-more">READ MORE »</span>
  <div class="stars"><svg width="72" height="14" viewBox="0 0 72 14"><g fill="#f06a1b"><use href="#s"/><use href="#s" x="19"/><use href="#s" x="38"/><use href="#s" x="57"/></g></svg></div>
</article>
<article class="review-card abs" style="left:614px">
  <div class="review-photo abs" style="background:linear-gradient(135deg,#8fb6d8,#c9d6e2 60%,#e8d9c8)" role="img" aria-label="Friends smiling in a car"><div class="avatar abs" role="img" aria-label="Reviewer portrait"></div></div>
  <h4>SED UT PERSPICIATIS UNDE OMNIS ISTE NATUS.</h4>
  <p>Lorem ipsum dolor sit amet, consectetur adipisicing elit, sed do eiusmod tempor incidid.</p>
  <span class="read-more">READ MORE »</span>
  <div class="stars"><svg width="72" height="14" viewBox="0 0 72 14"><g fill="#f06a1b"><use href="#s"/><use href="#s" x="19"/><use href="#s" x="38"/><use href="#s" x="57"/></g></svg></div>
</article>
<article class="review-card abs" style="left:890px">
  <div class="review-photo abs" style="background:linear-gradient(135deg,#f0f0f0,#9aa4b0 50%,#1c2536)" role="img" aria-label="Driver using a dashboard screen"><div class="avatar abs" role="img" aria-label="Reviewer portrait"></div></div>
  <h4>SED UT PERSPICIATIS UNDE OMNIS ISTE NATUS.</h4>
  <p>Lorem ipsum dolor sit amet, consectetur adipisicing elit, sed do eiusmod tempor incidid.</p>
  <span class="read-more">READ MORE »</span>
  <div class="stars"><svg width="72" height="14" viewBox="0 0 72 14"><g fill="#f06a1b"><use href="#s"/><use href="#s" x="19"/><use href="#s" x="38"/><use href="#s" x="57"/></g></svg></div>
</article>

<div class="round-arrow abs" style="left:60px;background:var(--navy)"><svg width="10" height="12" viewBox="0 0 10 12"><path d="M7 1 2 6l5 5" fill="none" stroke="#fff" stroke-width="2.5"/></svg></div>
<div class="round-arrow abs" style="left:98px;background:#555"><svg width="10" height="12" viewBox="0 0 10 12"><path d="M3 1l5 5-5 5" fill="none" stroke="#fff" stroke-width="2.5"/></svg></div>
<div class="view-all abs">VIEW ALL</div>

<section class="software abs">
  <div class="software-photo abs" role="img" aria-label="Hand touching a navigation map on a car dashboard screen"></div>
  <h2>OUR REVIEW<br>SOFTWARE</h2>
  <p class="lead">Lorem ipsum dolor sit amet, consectetur adipiscing elit, sed do eiusmod tempor incididunt ut labore et</p>
  <p class="body">Ut enim ad minim veniam, quis nostrud exercitation ullamco laboris nisi ut aliquip ex ea commodo consequat. Duis aute irure dolor in reprehenderit in voluptate velit esse cillum dolore eu fugiat nulla pariatur.Lorem ipsum dolor sit amet, consectetur adipiscing elit, sed do eiusmod tempor incididunt ut labore et dolore magna aliqua.</p>
  <div class="read">READ MORE</div>
</section>

<section class="map abs" role="img" aria-label="Street map showing the office location">
  <svg class="abs" style="left:697px;top:68px" width="84" height="112" viewBox="0 0 84 112"><path d="M42 110C20 78 2 60 2 40a40 40 0 0 1 80 0c0 20-18 38-40 70z" fill="var(--navy)"/><circle cx="42" cy="40" r="22" fill="#fff"/></svg>
  <div class="map-card abs">Lorium ipsum,<br>Dolor amit,NZ.</div>
  <div class="map-btn abs" style="left:503px;background:var(--royal)"><svg width="24" height="28" viewBox="0 0 24 28"><path d="M2 4h20v20H2z" fill="none" stroke="#fff" stroke-width="2"/><path d="M12 20c-4-5-5-7-5-9a5 5 0 0 1 10 0c0 2-1 4-5 9z" fill="#fff"/></svg></div>
  <div class="map-btn abs" style="left:573px"><svg width="36" height="26" viewBox="0 0 36 26"><rect x="1" y="1" width="34" height="24" rx="2" fill="none" stroke="#444" stroke-width="2"/><path d="M1 2l17 13L35 2" fill="none" stroke="#444" stroke-width="2"/></svg></div>
  <div class="map-btn abs" style="left:640px"><svg width="32" height="32" viewBox="0 0 32 32"><path d="M6 3l6 1 2 7-4 3c2 4 4 6 8 8l3-4 7 2 1 6c-1 2-3 3-5 3C13 28 4 19 3 7c0-2 1-3 3-4z" fill="none" stroke="#444" stroke-width="1.8"/></svg></div>
</section>

<h2 class="section-title abs" style="top:4284px">VISIBILITY AUDIT</h2>
<div class="stat abs" style="left:80px"><div class="num">60%</div><div class="label">Lorium ipsum</div><div class="btn">LEARN MORE</div></div>
<div class="stat abs" style="left:340px"><div class="num">40%</div><div class="label">Lorium ipsum</div><div class="btn">LEARN MORE</div></div>
<div class="stat abs" style="left:599px"><div class="num">70%</div><div class="label">Lorium ipsum</div><div class="btn">LEARN MORE</div></div>
<div class="stat abs" style="left:860px"><div class="num">90%</div><div class="label">Lorium ipsum</div><div class="btn">LEARN MORE</div></div>

<footer class="site-footer abs">
  <nav class="footer-nav abs"><a href="#">HOME</a><a href="#">ABOUT US</a><a href="#">SERVICES</a><a href="#">REVIEWS</a><a href="#">CONTACT US</a></nav>
  <div class="socials abs"><span></span><span></span><span></span><span></span></div>
  <div class="newsletter abs">
    <svg class="abs" style="left:20px;top:17px" width="32" height="24" viewBox="0 0 32 24"><rect x="1" y="1" width="30" height="22" rx="2" fill="none" stroke="#555" stroke-width="1.5"/><path d="M5 6h12M5 10h8" stroke="#555" stroke-width="1.5"/><rect x="21" y="5" width="6" height="6" fill="none" stroke="#555" stroke-width="1.5"/></svg>
    <span class="field">Enter your email for out newsletter</span>
    <div class="join">JOIN</div>
  </div>
  <p class="copyright abs">© Copyright 2019 - www.brightpathoutreach.com</p>
</footer>

</body>
</html>
```